Professionelles Design für Use Case Präsentationen im B2B-Bereich

Wir sind ein Schweizer Technologieunternehmen (Veltaro GmbH, www.veltaro-beispiel.ch), das datenbasierte Simulationen, Optimierung und Entscheidungsunterstützung für Unternehmen in Logistik, Produktion und Verkehr anbietet.
Ziel dieses Projekts ist es, bestehende Use Cases in ein modernes, visuell ansprechendes Format zu bringen, das unsere Kompetenz und den Nutzen für Kunden klar kommuniziert. Die Zielgruppe sind Entscheidungsträger in mittleren bis großen Industrieunternehmen (Bereichsleiter, Projektleiter, Geschäftsleitung).
Was wir brauchen:
– Ein cleanes, professionelles Design (PowerPoint oder PDF-Layout), das sich gut für Präsentationen, Whitepaper oder als LinkedIn-Content eignet.
– Klare Struktur mit Infografiken, Icons, Diagrammen oder Visualisierungen.
– Integration unseres Logos, Farbschemas und ggf. unseres Slogans.
Stilrichtung:
– Modern, technisch fundiert, aber nicht überladen
– Klar, direkt, seriös
– Gerne mit einem visuellen roten Faden (z. B. durchgängige Icons oder Layout-Struktur)
Ein Beispieldokument (UseCase Transportkosten) mit Inhalte ist angefügt. Ziel ist eine wiederverwendbare Vorlage, die wir für verschiedene Kunden-Use-Cases adaptieren können.
- Roboto

```html
<!DOCTYPE html>
<html lang="de">
<head>
<meta charset="utf-8">
<title>Veltaro – Use Case Transportkosten</title>
<link rel="stylesheet" href="https://fonts.googleapis.com/css2?family=Archivo:wdth,wght@125,800;125,900&family=Roboto:wght@400;500;700&display=swap">
<style>
  :root{
    --forest:#2a3320;
    --forest-deep:#222a19;
    --olive:#d2ce62;
    --olive-light:#e4e08f;
    --ink:#1d1d1b;
    --body:#3a3a36;
    --rule:#d9d6a0;
    --paper:#ffffff;
    --frame:#bdbdbd;
  }
  *{box-sizing:border-box;margin:0;padding:0}
  html,body{width:1004px;height:1200px;overflow:hidden;background:var(--paper)}
  body{position:relative;font-family:"Roboto",Arial,sans-serif;color:var(--body)}

  .panel{position:absolute;width:595px;height:335px;overflow:hidden;background:var(--paper);border:1px solid var(--frame)}
  .panel--small{transform-origin:0 0;transform:scale(.7311,.7343)}
  .panel--p1{left:57px;top:73px}
  .panel--p2{left:513px;top:73px}
  .panel--p3{left:205px;top:397px}
  .panel--p4{left:205px;top:788px}

  .display{font-family:"Archivo","Arial Black",sans-serif;font-stretch:125%;font-weight:900;text-transform:uppercase;letter-spacing:.5px}

  .header{position:absolute;left:0;top:0;width:100%;background:linear-gradient(100deg,var(--forest) 55%,#34402a 80%,var(--forest) 100%)}
  .header--hero{height:178px}
  .header--compact{height:101px}
  .header-rule{position:absolute;left:0;height:3px;width:338px;background:var(--olive)}
  .header--hero + .header-rule{top:182px}
  .header--compact + .header-rule{top:104px}

  .brand{position:absolute;display:flex;align-items:center;gap:9px}
  .brand-dot{width:34px;height:34px;border-radius:50%;border:3px solid var(--olive);background:transparent}
  .brand-name{font-family:"Archivo","Arial Black",sans-serif;font-stretch:125%;font-weight:800;color:var(--olive);font-size:24px;letter-spacing:.5px}
  .panel--hero .brand{left:32px;top:24px}
  .panel--data .brand{left:448px;top:18px}
  .panel--data .brand-dot{width:26px;height:26px;border-width:2.5px}
  .panel--data .brand-name{font-size:18px}

  .headline{position:absolute;color:var(--olive);font-size:25px;line-height:1}
  .subline{position:absolute;color:#fff;font-size:16px;line-height:19.5px}
  .panel--hero .headline{left:32px;top:80px}
  .panel--hero .subline{left:32px;top:108px}
  .panel--data .headline{left:28px;top:21px}
  .panel--data .subline{left:28px;top:49px;font-size:15.5px;line-height:17.5px}

  .hero-visual{position:absolute;left:360px;top:-4px;width:235px;height:200px}

  .facts{position:absolute;left:0;top:204px;width:100%;height:94px}
  .fact{position:absolute;top:0}
  .fact-icon{position:absolute;left:0;top:0;width:22px;height:22px}
  .fact-title{position:absolute;top:0;left:27px;color:var(--ink);font-size:10.5px;line-height:11px;white-space:nowrap}
  .fact-text{position:absolute;top:27px;left:27px;font-size:7.2px;line-height:8.4px;color:var(--body);white-space:nowrap}
  .fact--start{left:20px}
  .fact--solution{left:162px}
  .fact--benefit{left:334px}
  .fact--voice{left:472px}
  .benefits{list-style:none}
  .benefits li{position:relative;line-height:7.6px;margin-bottom:2.4px}
  .benefits li::before{content:"›";position:absolute;left:-8px;top:-1px;font-size:9px;font-weight:700;color:var(--olive)}
  .divider{position:absolute;top:206px;width:1px;height:86px;background:var(--rule)}
  .divider--a{left:152px}.divider--b{left:325px}.divider--c{left:463px}

  .media-map{position:absolute;left:59px;top:121px;width:279px;height:166px;border:1px solid #9a9a9a;background:linear-gradient(135deg,#dfe7cf 0%,#e8ecd9 40%,#cfdcc0 70%,#d9e3ea 100%)}
  .dashboard{position:absolute;left:370px;top:120px;width:168px;height:167px;border:1px solid #9a9a9a;background:#fff;padding:4px}
  .dash-title{font-size:5.6px;text-align:center;color:var(--ink);margin-bottom:4px}
  .dash-kpis{display:flex;gap:2px;margin-bottom:4px}
  .dash-kpis span{flex:1;height:6px;border-top:1px solid #bbb;border-bottom:1px solid #e2e2e2}
  .dash-map{height:48px;background:linear-gradient(135deg,#ececec,#e2e2e2);margin-bottom:4px}
  .dash-table{height:30px;background:repeating-linear-gradient(#fff 0 2.5px,#d6d6d6 2.5px 3px);margin-bottom:4px}

  .footer{position:absolute;left:0;top:300px;width:100%;height:35px}
  .cta{position:absolute;left:20px;top:6px;color:var(--olive);font-size:16.5px}
  .cta-note{position:absolute;left:169px;top:5px;font-size:7.3px;line-height:8.6px;color:var(--ink)}
  .footer-band{position:absolute;left:262px;top:6px;width:333px;height:29px}
  .phone{position:absolute;left:286px;top:9px;font-family:"Archivo","Arial Black",sans-serif;font-stretch:125%;font-weight:800;font-size:16.5px;line-height:20px;color:var(--forest-deep)}
  .mail{position:absolute;left:436px;top:13px;font-size:8.6px;line-height:10px;color:var(--forest-deep);font-weight:400}
</style>
</head>
<body>

<!-- ============ Hero layout (small) ============ -->
<section class="panel panel--hero panel--small panel--p1">
  <div class="header header--hero"></div><div class="header-rule"></div>
  <div class="brand"><span class="brand-dot"></span><span class="brand-name">Veltaro</span></div>
  <h1 class="headline display">Was wäre, wenn…</h1>
  <p class="subline display">…Sie neue Standorte<br>mit echten Transportkosten<br>vergleichen könnten?</p>
  <svg class="hero-visual" viewBox="0 0 235 200">
    <circle cx="118" cy="104" r="104" fill="#111"/>
    <path d="M40 40 A104 104 0 0 1 200 18 L186 30 A92 92 0 0 0 48 52 Z" fill="#d2ce62"/>
    <circle cx="108" cy="96" r="100" fill="#fff"/>
    <circle cx="110" cy="98" r="92" fill="url(#heroFillA)" role="img" aria-label="Globus mit Flugzeug, Lastwagen und Paketstapeln"/>
    <defs><radialGradient id="heroFillA" cx="45%" cy="35%" r="70%"><stop offset="0" stop-color="#8cc3e6"/><stop offset=".55" stop-color="#c9a77a"/><stop offset="1" stop-color="#f4efe6"/></radialGradient></defs>
  </svg>
  <div class="divider divider--a"></div><div class="divider divider--b"></div><div class="divider divider--c"></div>
  <div class="facts">
    <div class="fact fact--start">
      <svg class="fact-icon" viewBox="0 0 22 22" fill="none" stroke="#d2ce62" stroke-width="1.4"><circle cx="11" cy="11" r="9.5"/><circle cx="11" cy="11" r="6"/><circle cx="11" cy="11" r="2.5"/><path d="M11 11 L20 2"/></svg>
      <h2 class="fact-title display">Ausgangslage<br>&amp; Ziel</h2>
      <p class="fact-text">Ein Handelsunternehmen<br>prüfte mehrere neue Stan-<br>dorte. Dabei ging es um die<br>Frage: Wie verändern sich<br>die Transportkosten und die<br>Kundenbelieferung bei<br>einem Umzug?</p>
    </div>
    <div class="fact fact--solution">
      <svg class="fact-icon" viewBox="0 0 22 22" fill="none" stroke="#d2ce62" stroke-width="1.3"><path d="M11 4a5.5 5.5 0 0 0-3.2 10v3h6.4v-3A5.5 5.5 0 0 0 11 4z"/><path d="M8.5 19.5h5M11 0.5v2M3 3l1.5 1.5M19 3l-1.5 1.5M1 10h2M19 10h2"/></svg>
      <h2 class="fact-title display">Die Lösung<br>unsere Simulation</h2>
      <p class="fact-text">Wir kombinierten Standortdat-<br>en, Kundenadressen und Liefer-<br>mengen mit einem automatis-<br>ierten Tourenplaner. So wurden<br>die neuen Transportkosten und<br>Fahrzeiten für alle Varianten<br>berechnet und visualisiert.</p>
    </div>
    <div class="fact fact--benefit">
      <svg class="fact-icon" viewBox="0 0 22 22" fill="none" stroke="#d2ce62" stroke-width="1.6"><path d="M2 20h18"/><path d="M5 17v-4M10 17v-7M15 17V7"/><path d="M3 10l6-5 4 3 6-6M15 2h4v4"/></svg>
      <h2 class="fact-title display">Der konkrete<br>Nutzen</h2>
      <ul class="fact-text benefits">
        <li>Vergleich der Standorte mit<br>echten Touren</li>
        <li>Transparente Berechnung<br>der Transportkosten</li>
        <li>Klare Entscheidungsgrund-<br>lage für Geschäftsleitung</li>
        <li>Erste Resultate in weniger<br>als 3 Wochen</li>
      </ul>
    </div>
    <div class="fact fact--voice">
      <svg class="fact-icon" viewBox="0 0 22 22" fill="none" stroke="#d2ce62" stroke-width="1.3"><path d="M2 5h13v10H8l-4 4v-4H2z"/><path d="M5 9h7M5 12h5"/><path d="M18 2l1 2 2 .3-1.5 1.4.4 2L18 6.7 16.1 7.7l.4-2L15 4.3l2-.3z"/></svg>
      <h2 class="fact-title display">Kunden<br>Feedback</h2>
      <p class="fact-text">„Wir wussten genau,<br>welcher Standort für<br>unsere Kundenbe-<br>lieferung am effizien-<br>testen ist – daten-<br>basiert und nachvoll-<br>ziehbar.“</p>
    </div>
  </div>
  <footer class="footer">
    <span class="cta display">Jetzt testen</span>
    <p class="cta-note">Standortentscheidung<br>absichern mit Simulation</p>
    <svg class="footer-band" viewBox="0 0 333 29" preserveAspectRatio="none">
      <defs><linearGradient id="bandA" x1="0" x2="1"><stop offset="0" stop-color="#d2ce62"/><stop offset="1" stop-color="#e4e08f"/></linearGradient></defs>
      <polygon points="6,0 14,0 8,29 0,29" fill="#2a3320"/>
      <polygon points="20,0 333,0 333,29 14,29" fill="url(#bandA)"/>
      <g stroke="#fff" stroke-width="3"><path d="M282 29 L296 0M294 29 L308 0M306 29 L320 0M318 29 L332 0"/></g>
    </svg>
    <span class="phone">+41 44 555 01 23</span>
    <span class="mail">info@veltaro-beispiel.ch</span>
  </footer>
</section>

<!-- ============ Data layout (small) ============ -->
<section class="panel panel--data panel--small panel--p2">
  <div class="header header--compact"></div><div class="header-rule"></div>
  <div class="brand"><span class="brand-dot"></span><span class="brand-name">Veltaro</span></div>
  <h1 class="headline display">Was wäre, wenn…</h1>
  <p class="subline display">…Sie neue Standorte mit echten<br>Transportkosten vergleichen könnten?</p>
  <div class="media-map" role="img" aria-label="Karte der Schweiz mit Standorten und Kundenpunkten"></div>
  <div class="dashboard">
    <p class="dash-title">Beispiel Tourenplanung Auswertung</p>
    <div class="dash-kpis"><span></span><span></span><span></span><span></span><span></span></div>
    <div class="dash-map"></div>
    <div class="dash-table"></div>
    <svg viewBox="0 0 160 44" width="160" height="44">
      <g fill="#5b6ee1"><rect x="4" y="14" width="4" height="28"/><rect x="40" y="24" width="4" height="18"/></g>
      <g fill="#e0457b"><rect x="9" y="20" width="4" height="22"/><rect x="30" y="26" width="4" height="16"/></g>
      <g fill="#f29b38"><rect x="14" y="22" width="4" height="20"/><rect x="35" y="30" width="4" height="12"/></g>
      <g fill="#3cb8c9"><rect x="19" y="18" width="4" height="24"/><rect x="25" y="28" width="4" height="14"/></g>
      <g fill="#8b4fc8"><rect x="90" y="6" width="4" height="36"/><rect x="110" y="20" width="4" height="22"/></g>
      <g fill="#f29b38"><rect x="95" y="16" width="4" height="26"/></g>
      <g fill="#3cb8c9"><rect x="100" y="14" width="4" height="28"/></g>
      <g fill="#e0457b"><rect x="105" y="22" width="4" height="20"/></g>
      <path d="M2 42H70M82 42H150" stroke="#999" stroke-width=".6"/>
    </svg>
  </div>
  <footer class="footer">
    <span class="cta display">Jetzt testen</span>
    <p class="cta-note">Standortentscheidung<br>absichern mit Simulation</p>
    <svg class="footer-band" viewBox="0 0 333 29" preserveAspectRatio="none">
      <defs><linearGradient id="bandB" x1="0" x2="1"><stop offset="0" stop-color="#d2ce62"/><stop offset="1" stop-color="#e4e08f"/></linearGradient></defs>
      <polygon points="6,0 14,0 8,29 0,29" fill="#2a3320"/>
      <polygon points="20,0 333,0 333,29 14,29" fill="url(#bandB)"/>
      <g stroke="#fff" stroke-width="3"><path d="M282 29 L296 0M294 29 L308 0M306 29 L320 0M318 29 L332 0"/></g>
    </svg>
    <span class="phone">+41 44 555 01 23</span>
    <span class="mail">info@veltaro-beispiel.ch</span>
  </footer>
</section>

<!-- ============ Hero layout (large) ============ -->
<section class="panel panel--hero panel--p3">
  <div class="header header--hero"></div><div class="header-rule"></div>
  <div class="brand"><span class="brand-dot"></span><span class="brand-name">Veltaro</span></div>
  <h1 class="headline display">Was wäre, wenn…</h1>
  <p class="subline display">…Sie neue Standorte<br>mit echten Transportkosten<br>vergleichen könnten?</p>
  <svg class="hero-visual" viewBox="0 0 235 200">
    <circle cx="118" cy="104" r="104" fill="#111"/>
    <path d="M40 40 A104 104 0 0 1 200 18 L186 30 A92 92 0 0 0 48 52 Z" fill="#d2ce62"/>
    <circle cx="108" cy="96" r="100" fill="#fff"/>
    <circle cx="110" cy="98" r="92" fill="url(#heroFillC)" role="img" aria-label="Globus mit Flugzeug, Lastwagen und Paketstapeln"/>
    <defs><radialGradient id="heroFillC" cx="45%" cy="35%" r="70%"><stop offset="0" stop-color="#8cc3e6"/><stop offset=".55" stop-color="#c9a77a"/><stop offset="1" stop-color="#f4efe6"/></radialGradient></defs>
  </svg>
  <div class="divider divider--a"></div><div class="divider divider--b"></div><div class="divider divider--c"></div>
  <div class="facts">
    <div class="fact fact--start">
      <svg class="fact-icon" viewBox="0 0 22 22" fill="none" stroke="#d2ce62" stroke-width="1.4"><circle cx="11" cy="11" r="9.5"/><circle cx="11" cy="11" r="6"/><circle cx="11" cy="11" r="2.5"/><path d="M11 11 L20 2"/></svg>
      <h2 class="fact-title display">Ausgangslage<br>&amp; Ziel</h2>
      <p class="fact-text">Ein Handelsunternehmen<br>prüfte mehrere neue Stan-<br>dorte. Dabei ging es um die<br>Frage: Wie verändern sich<br>die Transportkosten und die<br>Kundenbelieferung bei<br>einem Umzug?</p>
    </div>
    <div class="fact fact--solution">
      <svg class="fact-icon" viewBox="0 0 22 22" fill="none" stroke="#d2ce62" stroke-width="1.3"><path d="M11 4a5.5 5.5 0 0 0-3.2 10v3h6.4v-3A5.5 5.5 0 0 0 11 4z"/><path d="M8.5 19.5h5M11 0.5v2M3 3l1.5 1.5M19 3l-1.5 1.5M1 10h2M19 10h2"/></svg>
      <h2 class="fact-title display">Die Lösung<br>unsere Simulation</h2>
      <p class="fact-text">Wir kombinierten Standortdat-<br>en, Kundenadressen und Liefer-<br>mengen mit einem automatis-<br>ierten Tourenplaner. So wurden<br>die neuen Transportkosten und<br>Fahrzeiten für alle Varianten<br>berechnet und visualisiert.</p>
    </div>
    <div class="fact fact--benefit">
      <svg class="fact-icon" viewBox="0 0 22 22" fill="none" stroke="#d2ce62" stroke-width="1.6"><path d="M2 20h18"/><path d="M5 17v-4M10 17v-7M15 17V7"/><path d="M3 10l6-5 4 3 6-6M15 2h4v4"/></svg>
      <h2 class="fact-title display">Der konkrete<br>Nutzen</h2>
      <ul class="fact-text benefits">
        <li>Vergleich der Standorte mit<br>echten Touren</li>
        <li>Transparente Berechnung<br>der Transportkosten</li>
        <li>Klare Entscheidungsgrund-<br>lage für Geschäftsleitung</li>
        <li>Erste Resultate in weniger<br>als 3 Wochen</li>
      </ul>
    </div>
    <div class="fact fact--voice">
      <svg class="fact-icon" viewBox="0 0 22 22" fill="none" stroke="#d2ce62" stroke-width="1.3"><path d="M2 5h13v10H8l-4 4v-4H2z"/><path d="M5 9h7M5 12h5"/><path d="M18 2l1 2 2 .3-1.5 1.4.4 2L18 6.7 16.1 7.7l.4-2L15 4.3l2-.3z"/></svg>
      <h2 class="fact-title display">Kunden<br>Feedback</h2>
      <p class="fact-text">„Wir wussten genau,<br>welcher Standort für<br>unsere Kundenbe-<br>lieferung am effizien-<br>testen ist – daten-<br>basiert und nachvoll-<br>ziehbar.“</p>
    </div>
  </div>
  <footer class="footer">
    <span class="cta display">Jetzt testen</span>
    <p class="cta-note">Standortentscheidung<br>absichern mit Simulation</p>
    <svg class="footer-band" viewBox="0 0 333 29" preserveAspectRatio="none">
      <defs><linearGradient id="bandC" x1="0" x2="1"><stop offset="0" stop-color="#d2ce62"/><stop offset="1" stop-color="#e4e08f"/></linearGradient></defs>
      <polygon points="6,0 14,0 8,29 0,29" fill="#2a3320"/>
      <polygon points="20,0 333,0 333,29 14,29" fill="url(#bandC)"/>
      <g stroke="#fff" stroke-width="3"><path d="M282 29 L296 0M294 29 L308 0M306 29 L320 0M318 29 L332 0"/></g>
    </svg>
    <span class="phone">+41 44 555 01 23</span>
    <span class="mail">info@veltaro-beispiel.ch</span>
  </footer>
</section>

<!-- ============ Data layout (large) ============ -->
<section class="panel panel--data panel--p4">
  <div class="header header--compact"></div><div class="header-rule"></div>
  <div class="brand"><span class="brand-dot"></span><span class="brand-name">Veltaro</span></div>
  <h1 class="headline display">Was wäre, wenn…</h1>
  <p class="subline display">…Sie neue Standorte mit echten<br>Transportkosten vergleichen könnten?</p>
  <div class="media-map" role="img" aria-label="Karte der Schweiz mit Standorten und Kundenpunkten"></div>
  <div class="dashboard">
    <p class="dash-title">Beispiel Tourenplanung Auswertung</p>
    <div class="dash-kpis"><span></span><span></span><span></span><span></span><span></span></div>
    <div class="dash-map"></div>
    <div class="dash-table"></div>
    <svg viewBox="0 0 160 44" width="160" height="44">
      <g fill="#5b6ee1"><rect x="4" y="14" width="4" height="28"/><rect x="40" y="24" width="4" height="18"/></g>
      <g fill="#e0457b"><rect x="9" y="20" width="4" height="22"/><rect x="30" y="26" width="4" height="16"/></g>
      <g fill="#f29b38"><rect x="14" y="22" width="4" height="20"/><rect x="35" y="30" width="4" height="12"/></g>
      <g fill="#3cb8c9"><rect x="19" y="18" width="4" height="24"/><rect x="25" y="28" width="4" height="14"/></g>
      <g fill="#8b4fc8"><rect x="90" y="6" width="4" height="36"/><rect x="110" y="20" width="4" height="22"/></g>
      <g fill="#f29b38"><rect x="95" y="16" width="4" height="26"/></g>
      <g fill="#3cb8c9"><rect x="100" y="14" width="4" height="28"/></g>
      <g fill="#e0457b"><rect x="105" y="22" width="4" height="20"/></g>
      <path d="M2 42H70M82 42H150" stroke="#999" stroke-width=".6"/>
    </svg>
  </div>
  <footer class="footer">
    <span class="cta display">Jetzt testen</span>
    <p class="cta-note">Standortentscheidung<br>absichern mit Simulation</p>
    <svg class="footer-band" viewBox="0 0 333 29" preserveAspectRatio="none">
      <defs><linearGradient id="bandD" x1="0" x2="1"><stop offset="0" stop-color="#d2ce62"/><stop offset="1" stop-color="#e4e08f"/></linearGradient></defs>
      <polygon points="6,0 14,0 8,29 0,29" fill="#2a3320"/>
      <polygon points="20,0 333,0 333,29 14,29" fill="url(#bandD)"/>
      <g stroke="#fff" stroke-width="3"><path d="M282 29 L296 0M294 29 L308 0M306 29 L320 0M318 29 L332 0"/></g>
    </svg>
    <span class="phone">+41 44 555 01 23</span>
    <span class="mail">info@veltaro-beispiel.ch</span>
  </footer>
</section>

</body>
</html>
```